Belmora Wines

Hi all,

My name’s Liam Dowsett and I run a small wine brand based in the Canberra Wine District, Australia. I’m currently in the process of branding the business and am looking for a designer to help develop a new visual direction.

Background
I’ll be growing my own fruit from a leased vineyard site Named 'Wrenhollow' and my family’s property named 'Tibbard Vale', with a stronger emphasis on organic practices and site expression.

The Direction
The brand will centre around single vineyard wines, with each wine reflecting the unique site it comes from. I’d like the branding to support this idea of place, origin, and authenticity.

In terms of visual style, I’m drawn to something that is:

Simple and effective
A balance between traditional and modern
Clean, considered, and not overly decorative

Nothing too over-the-top, the goal is something timeless that lets the wine and vineyard story speak for itself.

At this stage, I’m mainly looking for:

Conceptual design direction / ideas
Label design (with potential to expand into broader branding)

I’m open to creative interpretation, so if the story resonates with you, I’d love to see how you would approach it.

Below I've attached an example of the bottle shape I will be using.

Cheers,
Liam

Colors
0054AA
0677BA
7BADD7
CADEEF
E8F1F8
FFC000
F8CF3A
FAE287
FDF2CF
FEFAEE

Requirements
Must have
• Mix of modern and traditional

```html
<!DOCTYPE html>
<html lang="en">
<head>
<meta charset="utf-8">
<title>Belmora Wines — Single Vineyard Labels</title>
<link rel="stylesheet" href="https://fonts.googleapis.com/css2?family=Cormorant+Garamond:wght@400;500&family=Zilla+Slab:wght@500&display=swap">
<style>
  :root {
    --page: #ffffff;
    --navy: #4d4c6c;
    --navy-light: #5e5e7e;
    --navy-ink: #3b3a5c;
    --gold: #b89c62;
    --gold-light: #c7ad78;
    --cream: #ede4d0;
    --cream-light: #f1eadb;
    --muted-gold: #cfc2a6;
    --muted-navy: #6d6c86;
  }
  * { margin: 0; padding: 0; box-sizing: border-box; }
  html, body {
    width: 1200px;
    height: 1200px;
    overflow: hidden;
    background: var(--page);
  }
  .label-set {
    position: relative;
    width: 1200px;
    height: 1200px;
    display: flex;
    justify-content: center;
    align-items: center;
    gap: 120px;
  }
  .label {
    position: relative;
    width: 440px;
    height: 640px;
    display: flex;
    flex-direction: column;
    align-items: center;
  }
  .label--red {
    background: linear-gradient(160deg, var(--navy) 0%, var(--navy-light) 100%);
    color: var(--gold);
  }
  .label--white {
    background: linear-gradient(160deg, var(--cream) 0%, var(--cream-light) 100%);
    color: var(--navy-ink);
  }
  .site-map {
    margin-top: 76px;
    width: 220px;
    height: 282px;
    border-radius: 46% 40% 44% 38% / 36% 42% 40% 44%;
  }
  .label--red .site-map { background: linear-gradient(150deg, var(--gold-light), var(--gold)); }
  .label--white .site-map { background: linear-gradient(150deg, var(--navy-light), var(--navy-ink)); }
  .wordmark {
    margin-top: 58px;
    font-family: "Cormorant Garamond", serif;
    font-weight: 500;
    font-size: 78px;
    line-height: 1;
    letter-spacing: 1px;
  }
  .label--white .wordmark { color: var(--navy-ink); }
  .variety {
    margin-top: 26px;
    font-family: "Zilla Slab", serif;
    font-weight: 500;
    font-size: 25px;
    letter-spacing: 2px;
    text-transform: uppercase;
  }
  .label--red .variety { color: var(--muted-gold); }
  .vineyard {
    margin-top: 2px;
    font-family: "Cormorant Garamond", serif;
    font-size: 16px;
    letter-spacing: 0.5px;
  }
  .vintage {
    font-family: "Cormorant Garamond", serif;
    font-size: 14px;
    letter-spacing: 0.5px;
  }
  .label--red .vineyard, .label--red .vintage { color: var(--muted-gold); }
  .label--white .vineyard, .label--white .vintage { color: var(--muted-navy); }
</style>
</head>
<body>
  <main class="label-set">
    <section class="label label--red">
      <div class="site-map" role="img" aria-label="Gold outline map of the vineyard site with a branching vine-root illustration"></div>
      <h1 class="wordmark">Belmora</h1>
      <p class="variety">Pinot Noir</p>
      <p class="vineyard">Wrenhollow Vineyard</p>
      <p class="vintage">2023</p>
    </section>
    <section class="label label--white">
      <div class="site-map" role="img" aria-label="Navy outline map of the vineyard site with a branching vine-root illustration"></div>
      <h2 class="wordmark">Belmora</h2>
      <p class="variety">Riesling</p>
      <p class="vineyard">Wrenhollow Vineyard</p>
      <p class="vintage">2023</p>
    </section>
  </main>
</body>
</html>
```